Basic Letterhead Design

We need a Letterhead design. Our company is in the financial services industry. We are a small bank who lends money. I have uploaded an example our current letterhead design. We would like a new one.

```html
<!DOCTYPE html>
<html lang="en">
<head>
<meta charset="utf-8">
<title>Harrowgate Lending – Letterhead</title>
<link rel="stylesheet" href="https://fonts.googleapis.com/css2?family=Poppins:wght@400;500&display=swap">
<style>
  :root {
    --backdrop: #e2e2e2;
    --paper: #ffffff;
    --brand-green: #284b39;
    --band-black: #000000;
    --ink: #2b2b2b;
    --ink-dark: #111111;
    --signature-fill: #ececec;
  }
  * { margin: 0; padding: 0; box-sizing: border-box; }
  html, body {
    width: 1200px; height: 1200px; overflow: hidden;
    background: var(--backdrop);
    font-family: "Poppins", sans-serif;
    color: var(--ink);
  }
  .letterhead {
    position: absolute; left: 197px; top: 30px;
    width: 806px; height: 1140px;
    background: var(--paper);
    overflow: hidden;
  }
  .side-band { position: absolute; left: 0; top: 0; width: 21px; height: 1140px; }
  .brand {
    position: absolute; left: 74px; top: 118px;
    display: flex; align-items: center; gap: 12px;
  }
  .brand-dot { width: 30px; height: 30px; border-radius: 50%; background: var(--brand-green); }
  .brand-name {
    font-size: 23px; font-weight: 500; color: var(--brand-green);
    letter-spacing: 0.5px;
  }
  .recipient {
    position: absolute; left: 75px; top: 230px;
    font-size: 14px; line-height: 21.7px;
  }
  .salutation { position: absolute; left: 75px; top: 394px; font-size: 14px; }
  .letter-body {
    position: absolute; left: 75px; top: 444px; width: 655px;
    font-size: 13.6px; line-height: 25.8px; text-align: justify;
  }
  .signature {
    position: absolute; left: 69px; top: 872px;
    width: 305px; height: 76px; border-radius: 6px;
    background: var(--signature-fill);
  }
  .footer {
    position: absolute; left: 78px; right: 73px; top: 1058px;
    font-size: 10.3px; line-height: 15px; color: var(--ink-dark);
  }
  .footer-address { position: absolute; left: 0; top: 0; }
  .footer-contact { position: absolute; left: 202px; top: -2px; }
  .contact-line { display: flex; align-items: center; gap: 4px; }
  .contact-line svg { width: 9px; height: 9px; }
  .footer-company { position: absolute; right: 0; top: 1px; text-align: right; }
</style>
</head>
<body>
  <main class="letterhead">
    <svg class="side-band" viewBox="0 0 21 1140" aria-hidden="true">
      <polygon points="0,0 21,0 21,795 0,781" fill="var(--brand-green)"/>
      <polygon points="0,790 21,804 21,1140 0,1140" fill="var(--band-black)"/>
    </svg>

    <header class="brand">
      <span class="brand-dot"></span>
      <span class="brand-name">HARROWGATE LENDING</span>
    </header>

    <address class="recipient" style="font-style:normal">
      Mr. Alan Marsh<br>
      President<br>
      Northfield Advisors<br>
      111 Street Name,<br>
      City State, 12345
    </address>

    <p class="salutation">Dear</p>

    <div class="letter-body">
      <p>Lorem ipsum dolor sit amet, consectetur adipiscing elit. Aenean ut ipsum eget massa hendrerit vestibulum vel in velit. Donec pretium neque velit.</p>
      <p>Aliquam porta lectus nec mauris ornare venenatis. Vivamus non est turpis, et cursus sem. Mauris vehicula erat in diam auctor at bibendum nisl lacinia.</p>
      <p>Morbi imperdiet neque vehicula nunc convallis gravida. Vestibulum iaculis pretium placerat. Integer consequat, est sit amet facilisis eleifend, nibh nibh varius orci, eget dapibus arcu dui non purus. Pellentesque in magna mauris. Duis enim sapien, dictum vitae condimentum a, pulvinar vel lacus. Mauris et molestie nibh. Vestibulum vitae nulla at metus elementum porta sit amet interdum elit. Nulla sollicitudin neque eu nulla volutpat congue.</p>
      <p>Etiam pellentesque, velit id dapibus fermentum, turpis sapien ornare dui, ac tincidunt ligula odio congue purus. Nunc sed ante dui, in porta lectus. Cras nec sem lorem. In hac habitasse platea dictumst. Maecenas id diam quis dui porta tristique. Sed id egestas felis. Donec ullamcorper mattis posuere. Phasellus fermentum eleifend tortor vel dapibus. Vestibulum ante ipsum.</p>
    </div>

    <div class="signature" role="img" aria-label="Handwritten signature of Alan Marsh"></div>

    <footer class="footer">
      <div class="footer-address">4200 Harbor Avenue<br>Suite #000 Oakridge, CA, 90000</div>
      <div class="footer-contact">
        <div class="contact-line">
          <svg viewBox="0 0 10 10" aria-hidden="true"><rect x="0.5" y="2" width="9" height="6.5" fill="none" stroke="currentColor"/><polyline points="0.5,2 5,6 9.5,2" fill="none" stroke="currentColor"/></svg>
          name@harrowgate.com
        </div>
        <div class="contact-line">
          <svg viewBox="0 0 10 10" aria-hidden="true"><path d="M2 1 L4 1 L4.6 3.4 L3.4 4.3 Q4.4 6.2 5.8 6.7 L6.7 5.5 L9 6.1 L9 8.2 Q4.8 8.8 1.6 4.8 Q1 2.8 2 1Z" fill="currentColor"/></svg>
          300-555-0190
        </div>
      </div>
      <div class="footer-company">HARROWGATE LENDING PTY LTD<br>ACN: 512 038 771</div>
    </footer>
  </main>
</body>
</html>
```